Business card design needed

We are a Custom Joinery and specialise in design, Manufacture and Installation of kitchens and cabinetry
We currently have a logo based on the northern star in red and black but are open to something that would look fresh and clean
Updates

Project Deadline Extended
Reason: Need a couple days to go through designs. Finding some designs that are great on front and others great on reverse. I would like to be able to comment and get the total look we are after.

Target Market(s)

30-50 year olds who are looking to renovate

Industry/Entity Type

Business

Contact Information for Business Card

Larchfield Fitouts
ABN 37 418 260 573
Colin Pratley - Cabinetmaker/Designer Licence No. 318570K

Requirements
Nice to have
• Maybe a nice fresh modern kitchen picture

```html
<!DOCTYPE html>
<html lang="en">
<head>
<meta charset="utf-8">
<title>Larchfield Fitouts – Business Cards</title>
<link rel="stylesheet" href="https://fonts.googleapis.com/css2?family=Tinos:wght@400;700&display=swap">
<style>
  :root {
    --bg-light: #e4e4e4;
    --bg-dark: #a8a8a8;
    --brand-red: #cc1f27;
    --charcoal: #3a3a3a;
    --ink: #2b2b2b;
    --white: #ffffff;
    --soft-white: #e6e6e6;
    --card-radius: 27px;
  }
  * { box-sizing: border-box; margin: 0; padding: 0; }
  html, body {
    width: 1200px; height: 703px; overflow: hidden;
  }
  body {
    position: relative;
    background: radial-gradient(ellipse at 50% 45%, var(--bg-light) 0%, #c9c9c9 55%, var(--bg-dark) 100%);
    font-family: "Tinos", "Times New Roman", serif;
  }
  .card {
    position: absolute;
    width: 551px; height: 315px;
    border-radius: var(--card-radius);
    overflow: hidden;
    box-shadow: 0 1px 4px rgba(0,0,0,0.25);
  }
  .card--front  { left: 36px;  top: 24px;  background: var(--white); }
  .card--dark   { left: 612px; top: 24px;  background: var(--charcoal); }
  .card--white  { left: 36px;  top: 368px; background: var(--white); }
  .card--red    { left: 612px; top: 368px; background: var(--brand-red); }

  .card__swoosh { position: absolute; left: 0; top: 0; width: 100%; height: 100%; }

  .brand {
    position: absolute; left: 0; right: 0;
    display: flex; align-items: center; justify-content: center; gap: 12px;
    font-weight: 400; letter-spacing: 1px; white-space: nowrap;
  }
  .brand__mark { display: block; }
  .brand--small { top: 72px; font-size: 27px; color: var(--ink); }
  .brand--small .brand__mark { width: 14px; height: 14px; background: var(--brand-red); }
  .brand--large { top: 120px; font-size: 38px; }
  .card--dark .brand--large { color: var(--white); }
  .card--white .brand--large { color: var(--ink); }
  .card--white .brand__mark { width: 18px; height: 18px; background: var(--brand-red); }
  .card--red .brand--large { color: var(--white); top: 132px; }

  .contact-name {
    position: absolute; left: 0; right: 0; top: 176px;
    text-align: center; color: var(--ink); font-size: 15px;
  }
  .contact-name__person { color: var(--brand-red); font-weight: 700; font-size: 20px; }

  .contact-details {
    position: absolute; left: 0; right: 0; top: 250px;
    text-align: center; color: var(--white); font-size: 14px; line-height: 27px;
  }
  .contact-details__row { display: flex; justify-content: center; align-items: center; }
  .contact-details__item { padding: 0 7px; }
  .contact-details__item + .contact-details__item { border-left: 1px solid rgba(255,255,255,0.8); line-height: 16px; }
  .contact-details__phone { display: inline-flex; align-items: center; gap: 3px; }
  .contact-details__phone svg { width: 12px; height: 12px; }

  .website {
    position: absolute; left: 0; right: 0;
    text-align: center; font-size: 15px; letter-spacing: 3.2px;
  }
  .card--dark .website { top: 285px; color: var(--soft-white); transform: translateY(-10px); }
  .card--white .website { top: 281px; color: var(--ink); transform: translateY(-2px); }
  .card--red .website { top: 275px; color: var(--soft-white); transform: translateY(-4px); }
</style>
</head>
<body>

  <section class="card card--front" aria-label="Front of business card">
    <svg class="card__swoosh" viewBox="0 0 551 315" preserveAspectRatio="none" aria-hidden="true">
      <path d="M0 180 Q275 262 551 180 L551 315 L0 315 Z" fill="var(--charcoal)"/>
      <path d="M0 199 Q275 272 551 189 L551 315 L0 315 Z" fill="var(--brand-red)"/>
    </svg>
    <div class="brand brand--small"><span class="brand__mark"></span>Larchfield Fitouts</div>
    <p class="contact-name"><span class="contact-name__person">Colin Pratley,</span> Cabinetmaker/Designer</p>
    <div class="contact-details">
      <p>Street Name, City Name, State, City Zip Code</p>
      <p class="contact-details__row">
        <span class="contact-details__item contact-details__phone">
          <svg viewBox="0 0 12 12" aria-hidden="true"><path d="M3 1 L5 3.2 L4 4.4 Q5 6.8 7.6 8 L8.8 7 L11 9 L9.6 10.8 Q4.8 10.6 1.2 2.4 Z" fill="var(--white)"/></svg>0123-456-789
        </span>
        <span class="contact-details__item">ABN 37 418 260 573</span>
        <span class="contact-details__item">Licence No. 318570K</span>
      </p>
    </div>
  </section>

  <section class="card card--dark" aria-label="Reverse of business card, charcoal">
    <div class="brand brand--large">Larchfield Fitouts</div>
    <p class="website">www.larchfieldfitouts.com</p>
  </section>

  <section class="card card--white" aria-label="Reverse of business card, white">
    <div class="brand brand--large"><span class="brand__mark"></span>Larchfield Fitouts</div>
    <p class="website">www.larchfieldfitouts.com</p>
  </section>

  <section class="card card--red" aria-label="Reverse of business card, red">
    <div class="brand brand--large">Larchfield Fitouts</div>
    <p class="website">www.larchfieldfitouts.com</p>
  </section>

</body>
</html>
```